Harlan Ridge Smokehouse Jamboree's 10th ever event needs a Poster! This Non-Profit is a blast

We need a totally NEW and FUN poster design to promote our tiny Kentucky town which hosts 40,000+ people who come to meet the TV Celebrity BBQ Pitmasters - who smoke meat for their fans. It is all about Beers, Bands, BBQ + Bourbon. We are a family event with Free music all weekend long.

Target Market(s)

People who love Beer, BBQ, Bands and Bourbon

Colors
ec1f27
0555a3

Requirements
Must have
• Please only use original art.
• High energy / Fresh / Young
• Name: Harlan Ridge Smokehouse Jamboree
• 10th ever
• Sept 4+5, 2020
• Bands, Beer, BBQ + Bourbon
• Hosted by: Copperfield Hollow Distillery
• 2817 Marlow Pike Ashby, KY 40198
• $5 admission - FREE MUSIC - FREE Parking
Nice to have
• Please only use original art. Trademarked images and logos will be rejected.

```html
<!DOCTYPE html>
<html lang="en">
<head>
<meta charset="utf-8">
<title>Harlan Ridge Smokehouse Jamboree – 10th Ever</title>
<link rel="stylesheet" href="https://fonts.googleapis.com/css2?family=Alfa+Slab+One&family=Archivo+Black&family=Oswald:wght@700&family=Montserrat:ital,wght@0,800;1,800&display=swap">
<style>
  :root{
    --frame:#3a2e3a;
    --cream:#fdf6c8;
    --blue:#0555a3;
    --blue-deep:#064a8f;
    --red:#ec1f27;
    --gold:#f5d27a;
    --orange:#f26a2e;
    --amber:#f7b733;
    --ink:#2f2430;
    --pig:#f3cfa8;
  }
  *{box-sizing:border-box;margin:0;padding:0}
  html,body{width:848px;height:1200px;overflow:hidden;background:var(--frame)}
  .poster{position:relative;width:848px;height:1200px;background:var(--frame);overflow:hidden}
  .poster__border{position:absolute;left:12px;top:12px;width:824px;height:1176px;background:var(--cream)}
  .sky{position:absolute;left:24px;top:24px;width:800px;height:728px;
    background:radial-gradient(circle at 62% 40%, #0a62b8 0%, var(--blue) 45%, var(--blue-deep) 100%)}
  .ground{position:absolute;left:24px;top:752px;width:800px;height:424px;background:var(--red)}
  .ground__floor{position:absolute;left:24px;top:1060px;width:800px;height:116px}

  .anniv{position:absolute;left:58px;top:50px;width:256px;height:180px}
  .anniv__shape{position:absolute;left:0;top:0}
  .anniv__num{position:absolute;left:120px;top:72px;font:400 92px/1 "Archivo Black",sans-serif;color:var(--red);letter-spacing:-4px}
  .anniv__th{position:absolute;left:250px;top:80px;font:400 20px/1 "Alfa Slab One",serif;color:var(--gold)}
  .anniv__ever{position:absolute;left:144px;top:174px;font:400 28px/1 "Archivo Black",sans-serif;color:var(--gold);letter-spacing:-1px}

  .title{position:absolute;left:360px;top:40px;width:440px;font:400 66px/0.98 "Alfa Slab One",serif;color:#fff;
    text-shadow:-5px 5px 0 var(--ink);letter-spacing:1px}
  .title span{display:block}

  .wordmark{position:absolute;left:34px;top:314px;width:790px;text-align:center;white-space:nowrap;
    font:400 92px/1 "Alfa Slab One",serif;color:var(--red);letter-spacing:-1px;
    -webkit-text-stroke:3px var(--blue);
    text-shadow:6px 3px 0 var(--gold),9px 5px 0 var(--blue),12px 10px 8px rgba(0,0,0,.35);
    transform:rotate(-3deg) scaleY(2.3);transform-origin:center}
  .subtitle{position:absolute;left:84px;top:502px;font:400 46px/1 "Archivo Black",sans-serif;color:#fff;
    letter-spacing:20px;text-shadow:-4px 4px 0 var(--ink);transform:rotate(4deg);transform-origin:left}
  .dates{position:absolute;left:566px;top:520px;font:400 24px/1 "Archivo Black",sans-serif;color:var(--gold);
    letter-spacing:1px;text-shadow:-3px 3px 0 var(--ink);white-space:nowrap}

  .mascot{position:absolute;left:20px;top:590px;width:440px;height:540px;border-radius:46% 46% 40% 40%;
    background:linear-gradient(180deg,var(--pig) 0%,var(--pig) 42%,#7b96ad 42%,#6f8aa2 100%)}

  .badge{position:absolute;left:446px;top:572px;width:322px;height:322px;border-radius:50%;
    background:var(--cream);padding:7px}
  .badge__ring{width:100%;height:100%;border-radius:50%;background:var(--red);padding:6px}
  .badge__core{width:100%;height:100%;border-radius:50%;background:linear-gradient(180deg,var(--orange) 0%,#f48a2c 55%,var(--amber) 100%)}
  .badge__top{position:absolute;left:0;top:0;width:322px;height:322px}
  .badge__bottom{position:absolute;left:41px;top:234px;width:240px;text-align:center;white-space:nowrap;
    font:700 32px/1 "Oswald",sans-serif;color:var(--ink);transform:rotate(-3deg)}

  .banner{position:absolute;left:432px;top:680px;width:364px;height:112px;background:var(--ink);
    border:3px solid var(--cream);transform:rotate(-3deg);color:var(--cream);text-align:center;
    font:italic 800 22px/1 "Montserrat",sans-serif;letter-spacing:4px;padding-top:14px}
  .banner__and{display:flex;align-items:center;justify-content:center;gap:10px;font-size:17px;margin:4px 0}
  .banner__and::before,.banner__and::after{content:"";width:80px;height:2px;background:var(--cream)}

  .fork{position:absolute;width:70px;height:230px;background:var(--ink);border-radius:6px}
  .fork--left{left:456px;top:890px;transform:rotate(14deg)}
  .fork--right{left:710px;top:890px;transform:rotate(-14deg)}

  .price{position:absolute;left:574px;top:940px;font:400 74px/1 "Archivo Black",sans-serif;color:var(--cream);
    text-shadow:-4px 4px 0 var(--ink);letter-spacing:-2px}
  .price__label{position:absolute;left:560px;top:1030px;font:400 18px/1 "Archivo Black",sans-serif;color:var(--cream);
    letter-spacing:1px;transform:rotate(-9deg);text-shadow:-2px 2px 0 var(--ink)}

  .footer{position:absolute;top:1150px;font:700 11px/1 "Montserrat",sans-serif;color:var(--ink);letter-spacing:.6px;text-transform:uppercase}
  .footer--host{left:100px}
  .footer--address{left:486px}
</style>
</head>
<body>
<main class="poster">
  <div class="poster__border"></div>
  <div class="sky"></div>
  <div class="ground"></div>
  <svg class="ground__floor" viewBox="0 0 800 116" preserveAspectRatio="none" aria-hidden="true">
    <path d="M0 60 Q400 -20 800 40 L800 116 L0 116 Z" fill="#fdf6c8"/>
  </svg>

  <div class="anniv">
    <svg class="anniv__shape" width="256" height="180" viewBox="0 0 256 180" aria-hidden="true">
      <polygon points="0,0 256,0 200,180 56,180" fill="#3a2e3a"/>
    </svg>
  </div>
  <div class="anniv__num">10</div>
  <div class="anniv__th">th</div>
  <div class="anniv__ever">EVER</div>

  <h1 class="title"><span>HARLAN</span><span>RIDGE</span></h1>
  <div class="wordmark">SMOKEHOUSE</div>
  <div class="subtitle">JAMBOREE</div>
  <p class="dates">SEPT 4+5, 2020</p>

  <div class="mascot" role="img" aria-label="Cartoon pig in blue overalls standing with thumbs in its straps"></div>

  <div class="badge">
    <div class="badge__ring"><div class="badge__core"></div></div>
    <svg class="badge__top" viewBox="0 0 322 322">
      <defs><path id="arc" d="M55 150 A108 108 0 0 1 270 150"/></defs>
      <text font-family="Oswald, sans-serif" font-weight="700" font-size="34" fill="#2f2430" letter-spacing="1">
        <textPath href="#arc" startOffset="50%" text-anchor="middle">BANDS, BEER</textPath>
      </text>
    </svg>
    <div class="badge__bottom">BBQ + BOURBON</div>
  </div>

  <div class="banner">
    <div>FREE MUSIC</div>
    <div class="banner__and">AND</div>
    <div>FREE PARKING</div>
  </div>

  <div class="fork fork--left" role="img" aria-label="Barbecue carving fork"></div>
  <div class="fork fork--right" role="img" aria-label="Barbecue carving fork"></div>

  <div class="price">$5</div>
  <div class="price__label">ADMISSION</div>

  <p class="footer footer--host">Hosted by: Copperfield Hollow Distillery</p>
  <p class="footer footer--address">2817 Marlow Pike Ashby, KY 40198</p>
</main>
</body>
</html>
```